Professional looking Roller Blind Discount Card that portrays quality at a value for money price!

We need a double sided business card designed as a discount card. Size 90mm wide x 55mm high.We would like it to look professional and portray quality at a value for money price point.I have uploaded a word document with a basic layout with the information we want included on each side of the card. Please put your own thought into the layout.

As per word document attached.

```html
<!DOCTYPE html>
<html lang="en">
<head>
<meta charset="UTF-8">
<title>Roller Blind Discount Card</title>
<link href="https://fonts.googleapis.com/css2?family=Lato:wght@700&family=Open+Sans:wght@400;700&family=Oswald:wght@400&display=swap" rel="stylesheet">
<style>
  :root {
    --bg: #ecebe8;
    --card: #ffffff;
    --blue: #29a6df;
    --blue-light: #bfe3f5;
    --ink: #1f1f1f;
    --rule: #d4d4d4;
    --photo-a: #6f8a5a;
    --photo-b: #c9ced0;
  }
  * { margin: 0; padding: 0; box-sizing: border-box; }
  html, body { width: 1200px; height: 900px; overflow: hidden; }
  body {
    position: relative;
    background: var(--bg);
    font-family: "Open Sans", Arial, sans-serif;
    color: var(--ink);
  }
  .card {
    position: absolute;
    background: var(--card);
    box-shadow: 3px 4px 8px rgba(0,0,0,.25);
    overflow: hidden;
  }
  .card--front { left: 330px; top: 90px; width: 555px; height: 344px; }
  .card--back  { left: 330px; top: 469px; width: 560px; height: 344px; }

  .centered { position: absolute; left: 0; right: 0; text-align: center; }

  .offer-title {
    top: 50px;
    font-family: "Lato", Arial, sans-serif;
    font-weight: 700; font-size: 25px; color: var(--blue);
  }
  .offer-lines { top: 80px; font-size: 16px; line-height: 21px; }

  .badges {
    position: absolute; top: 152px; left: 116px;
    display: flex; gap: 14px;
  }
  .badge {
    width: 98px; height: 86px; border-radius: 10px;
    background: var(--blue); color: #fff;
    font-family: "Oswald", "Arial Narrow", sans-serif;
    font-size: 15px; line-height: 17px; letter-spacing: -0.3px;
    display: flex; align-items: center; justify-content: center; text-align: center;
    padding: 0 6px;
  }
  .divider {
    position: absolute; top: 268px; left: 118px; width: 319px; height: 1px;
    background: var(--rule);
  }
  .call { font-size: 16px; }
  .card--front .call { top: 290px; left: -12px; }
  .card--back .call { top: 305px; left: -10px; }
  .call strong { font-weight: 700; }

  .back-title {
    top: 37px;
    font-family: "Lato", Arial, sans-serif;
    font-weight: 700; font-size: 24px; color: var(--blue);
  }
  .back-sub { top: 64px; font-size: 16px; }

  .photo {
    position: absolute; left: 0; top: 96px; width: 257px; height: 193px;
    background: linear-gradient(100deg, var(--photo-a) 0%, #8ea57a 55%, var(--photo-b) 100%);
  }
  .bubbles {
    position: absolute; left: 405px; top: 35px; width: 145px; height: 155px;
    background: radial-gradient(ellipse at center, var(--blue-light) 0%, rgba(191,227,245,0) 70%);
  }
  .selection {
    position: absolute; left: 330px; top: 105px; width: 150px; text-align: center;
    font-size: 18px; line-height: 22px;
  }
  .brand {
    position: absolute; left: 290px; top: 260px; width: 250px;
    display: flex; align-items: center; justify-content: center; gap: 8px;
    font-family: "Lato", Arial, sans-serif; font-weight: 700;
    font-size: 22px; color: var(--blue);
  }
  .brand-mark { width: 13px; height: 13px; background: var(--blue); }
</style>
</head>
<body>

<section class="card card--front">
  <h1 class="centered offer-title">25% OFF</h1>
  <p class="centered offer-lines">Quality Custom Made Roller Blinds<br>Blockout – Screen – Light Filtering</p>
  <div class="badges">
    <div class="badge">“FREE in Home Measure &amp; Quote”</div>
    <div class="badge">“Best Price Guarantee”</div>
    <div class="badge">“Family Owned &amp; Operated”</div>
  </div>
  <div class="divider"></div>
  <p class="centered call">Call <strong>0400 555 123</strong> Today!</p>
</section>

<section class="card card--back">
  <h2 class="centered back-title">ROLLER BLINDS</h2>
  <p class="centered back-sub">FREE in Home Measure &amp; Quote</p>
  <div class="photo" role="img" aria-label="Photo of a room with roller blinds above windows looking onto a green garden"></div>
  <div class="bubbles" role="img" aria-label="Light blue decorative bubbles"></div>
  <p class="selection">Huge Selection<br>Of Fabrics</p>
  <div class="brand"><span class="brand-mark"></span>BRIGHTLINE BLINDS</div>
  <p class="centered call">Call <strong>0400 555 123</strong> Today</p>
</section>

</body>
</html>
```